Plakat-Design für Pfandhaus gesucht
Zielgruppe
Wir sind ein Pfandhaus wir vergeben Pfandkredite gegen Wertgegenstände sowie Juwelier und Goldankauf aber in erster Linie steht das Pfandhaus .
Aufgabenstellung
Ich möchte gerne Plakate Buchen die an Straßen oder Hauswänden befestigt sind. Ca.3,5x3 Meter. Die Botschaft muss kurz und knapp sein da die Leute ja vorbeifahren.

```html
<!DOCTYPE html>
<html lang="de">
<head>
<meta charset="utf-8">
<title>Pfandkredit-Lorenz – Poster quer</title>
<link rel="stylesheet" href="https://fonts.googleapis.com/css2?family=Open+Sans:ital,wght@0,700;0,800;1,800&family=Barlow+Semi+Condensed:wght@400;700&display=swap">
<style>
  :root {
    --board: #000000;
    --gold-light: #c9a366;
    --gold-dark: #7f4c0a;
    --ink-brown: #5a3410;
    --shadow-brown: #8a6a3a;
    --white: #ffffff;
    --badge-red: #f2361c;
    --badge-ink: #111111;
  }
  html, body {
    margin: 0;
    padding: 0;
    width: 1200px;
    height: 849px;
    overflow: hidden;
    background: var(--board);
  }
  .board {
    position: relative;
    width: 1200px;
    height: 849px;
    background: var(--board);
  }
  .poster {
    position: absolute;
    left: 98px;
    top: 66px;
    width: 1004px;
    height: 700px;
    overflow: hidden;
    background: linear-gradient(to right, var(--gold-light) 0 490px, var(--gold-dark) 490px 100%);
    font-family: "Open Sans", sans-serif;
  }
  .headline {
    position: absolute;
    left: 0;
    top: 37px;
    width: 100%;
    margin: 0;
    text-align: center;
    font-weight: 800;
    font-size: 96px;
    line-height: 1;
    color: var(--white);
    text-shadow: 7px 7px 0 var(--shadow-brown);
    white-space: nowrap;
  }
  .headline .connector {
    font-style: italic;
    letter-spacing: 1px;
    margin: 0 24px 0 20px;
    position: relative;
    top: -6px;
    font-size: 84px;
  }
  .headline .word-geld { letter-spacing: 6px; }
  .subline {
    position: absolute;
    left: 0;
    top: 134px;
    width: 100%;
    margin: 0;
    text-align: center;
    font-weight: 700;
    font-size: 24px;
    color: var(--white);
  }
  .hero-visual {
    position: absolute;
    left: 304px;
    top: 208px;
    width: 396px;
    height: 331px;
    border-radius: 50%;
    background: linear-gradient(to right, #b88a3c 0 47%, #d49a78 47% 100%);
    box-shadow: 0 28px 24px -14px rgba(40, 20, 0, .55);
  }
  .badge {
    position: absolute;
    left: 748px;
    top: 152px;
    width: 220px;
    height: 220px;
  }
  .badge-text {
    position: absolute;
    left: 12px;
    top: 42px;
    width: 196px;
    margin: 0;
    text-align: center;
    font-weight: 800;
    font-size: 15.5px;
    line-height: 19px;
    color: var(--badge-ink);
    transform: rotate(9deg);
  }
  .badge-text .lead { display: block; margin-bottom: 5px; font-size: 16px; }
  .locations {
    position: absolute;
    left: 40px;
    top: 595px;
    margin: 0;
    font-weight: 800;
    font-size: 23px;
    line-height: 29.5px;
    color: var(--ink-brown);
  }
  .brand-name {
    position: absolute;
    left: 673px;
    top: 534px;
    width: 270px;
    text-align: center;
    font-weight: 700;
    font-size: 30px;
    line-height: 38px;
    color: var(--white);
  }
  .website {
    position: absolute;
    left: 674px;
    top: 652px;
    font-weight: 800;
    font-size: 24px;
    color: var(--white);
  }
  .caption {
    position: absolute;
    left: 52px;
    top: 788px;
    margin: 0;
    font-family: "Barlow Semi Condensed", sans-serif;
    font-size: 20px;
    color: var(--white);
  }
  .caption strong { font-weight: 700; margin-right: 8px; }
</style>
</head>
<body>
<main class="board">
  <section class="poster">
    <h1 class="headline"><span class="word-gold">GOLD</span><span class="connector">gegen</span><span class="word-geld">GELD</span></h1>
    <p class="subline">Machen Sie schnell Dinge zu Geld, die schon lange rumliegen.</p>

    <div class="hero-visual" role="img" aria-label="Goldener Armreif, der zur Hälfte in ein gerolltes Bündel Geldscheine übergeht"></div>

    <div class="badge">
      <svg width="220" height="220" viewBox="0 0 220 220" aria-hidden="true">
        <circle cx="110" cy="110" r="94" fill="var(--badge-red)"/>
        <circle cx="110" cy="110" r="96" fill="none" stroke="var(--badge-red)" stroke-width="16" stroke-linecap="round" stroke-dasharray="0 21.1"/>
      </svg>
      <p class="badge-text"><span class="lead">Wir beleihen</span>Schmuck, Uhren,<br>Gold- &amp; Silberwaren,<br>Technische Geräte,<br>PKWs, alle Arten<br>von Zweirädern</p>
    </div>

    <p class="locations">Sie finden uns in:<br>Saarbrücken Trier Mainz<br>Wiesbaden Kaiserslautern</p>

    <div class="brand-name">Matthias Lorenz<br>Pfandkredit</div>
    <div class="website">pfandkredit-lorenz.de</div>
  </section>
  <p class="caption"><strong>Pfandkredit-Lorenz</strong>Poster Quer / Entwurf</p>
</main>
</body>
</html>
```